Aisle signage for supermarket

Design Isle signs for Indian supermarket. Modern, Clear, legible. Would be nice to use our logo colours. Signs Will be double sided and measure 900mm width x 400mm height. Indian theme would be nice. Attached files shows description to go on each sign.
Font styles to use
Sans Serif
Colors
Designer to choose colors to be used in the design.

```html
<!DOCTYPE html>
<html lang="en">
<head>
<meta charset="utf-8">
<title>Aisle Sign – Biscuits, Cakes, Tea, Coffee, Savouries</title>
<link rel="stylesheet" href="https://fonts.googleapis.com/css2?family=Kanit:ital,wght@1,800&display=swap">
<style>
  :root {
    --stage: #222222;
    --red-deep: #a80804;
    --red: #c81a06;
    --orange: #e2661a;
    --amber: #eea12a;
    --gold: #f7c743;
    --outline: #4a0a08;
    --white: #ffffff;
  }
  html, body {
    margin: 0;
    padding: 0;
    width: 1200px;
    height: 686px;
    overflow: hidden;
    background: var(--stage);
  }
  .aisle-sign {
    position: absolute;
    left: 0;
    top: 76px;
    width: 1200px;
    height: 533px;
    display: block;
  }
  .sign-label {
    font-family: "Kanit", "Arial Black", sans-serif;
    font-weight: 800;
    font-style: italic;
    font-size: 112px;
    fill: var(--white);
    stroke: var(--outline);
    stroke-width: 16px;
    stroke-linejoin: round;
    paint-order: stroke fill;
    letter-spacing: 1px;
  }
</style>
</head>
<body>
<svg class="aisle-sign" viewBox="0 0 1200 533" xmlns="http://www.w3.org/2000/svg">
  <defs>
    <linearGradient id="sign-base" x1="0" y1="0" x2="1" y2="0.3">
      <stop offset="0" stop-color="var(--red-deep)"/>
      <stop offset="0.4" stop-color="var(--red)"/>
      <stop offset="0.75" stop-color="var(--orange)"/>
      <stop offset="1" stop-color="var(--amber)"/>
    </linearGradient>
    <radialGradient id="mandala-glow" cx="0.5" cy="0.5" r="0.5">
      <stop offset="0" stop-color="var(--gold)" stop-opacity="0.85"/>
      <stop offset="0.6" stop-color="var(--amber)" stop-opacity="0.45"/>
      <stop offset="1" stop-color="var(--orange)" stop-opacity="0"/>
    </radialGradient>
  </defs>

  <rect class="sign-base" width="1200" height="533" fill="url(#sign-base)"/>

  <g role="img" aria-label="Golden Indian mandala pattern decoration">
    <circle cx="1100" cy="460" r="330" fill="url(#mandala-glow)"/>
    <circle cx="1180" cy="120" r="160" fill="url(#mandala-glow)" opacity="0.6"/>
  </g>

  <g class="sign-frame" fill="none" stroke="var(--white)" stroke-width="3">
    <rect x="45" y="35" width="1110" height="461"/>
  </g>

  <g class="frame-ornaments" fill="var(--white)">
    <rect x="555" y="18" width="90" height="34" rx="17" role="img" aria-label="Ornamental scroll motif"/>
    <rect x="555" y="479" width="90" height="34" rx="17" role="img" aria-label="Ornamental scroll motif"/>
    <rect x="28" y="230" width="34" height="76" rx="17" role="img" aria-label="Ornamental scroll motif"/>
    <rect x="1138" y="230" width="34" height="76" rx="17" role="img" aria-label="Ornamental scroll motif"/>
  </g>

  <g class="sign-labels">
    <text class="sign-label" x="88" y="155">BISCUITS / CAKES</text>
    <text class="sign-label" x="92" y="299">TEA / COFFE</text>
    <text class="sign-label" x="88" y="440">SAVOURIES</text>
  </g>
</svg>
</body>
</html>
```